Sleek wordpress site for Harborline finish works

We are a commercial job shop that serves B2B, govt & LEO and retail clients.We need a wordpress site with 6 individual pages: homepage, coating, laser engraving, laser cutting, part marking, and contact us. I have attached an outline of the desired flow and sub headings for each page. I would like to incorporate the colors of the logo through out the site to be clean and sleek enough to appeal to B2B commercial clients yet be inviting enough for retail clients.

I would like to have easy picture functionality so photographs on each page can be updated easily.

Target Market(s)

B2B industrial & Govt and Military part marking, laser engraving and coating: machine shops, aerospace companies, tool manufactures. Retail: personalized gifts, Job Shop

Coding

Coded - Design and coding required

Font styles to use
Sans Serif
Other font styles liked:
• Open to suggestion

Colors
0255a3
3176b5
eaf1f7
cfdeed
ffffff

Requirements
Must have
• Clean easy to navigate flow, separate pages as indicated on attached outline, high class feel. Great picture functionality, professional and inviting feel,
• **update: needs to be optimized for mobile, should have a gallery function. Gallery can be an additional page or embedded
Nice to have
• Social media connectivity links,
Should not have
• crappy plugins that make back-end management difficult, no blog

```html
<!DOCTYPE html>
<html lang="en">
<head>
<meta charset="utf-8">
<title>Harborline finish works</title>
<link href="https://fonts.googleapis.com/css2?family=Open+Sans:wght@300;400;600;700&display=swap" rel="stylesheet">
<style>
:root{
  --brand:#0255a3;
  --brand-mid:#3176b5;
  --pale:#eaf1f7;
  --pale-2:#cfdeed;
  --white:#ffffff;
  --ink:#2a2f36;
  --muted:#6d737b;
  --header-bg:#f5f7fa;
  --band-bg:#f2f4f8;
  --field:#f3f4f6;
  --footer:#5b5b5b;
}
*{margin:0;padding:0;box-sizing:border-box}
html,body{width:1200px;height:2182px;overflow:hidden}
body{font-family:"Open Sans",Arial,sans-serif;color:var(--ink);background:var(--white);position:relative}
.abs{position:absolute}
.center{text-align:center}

/* header */
.site-header{left:0;top:0;width:1200px;height:119px;background:var(--header-bg)}
.brand-name{left:160px;top:30px;width:160px;display:flex;align-items:center;gap:8px;font-weight:700;font-size:15px;line-height:1.15;color:var(--brand)}
.brand-mark{width:14px;height:14px;border-radius:50%;background:var(--brand);flex:none}
.callout{left:560px;top:29px;font-size:16px;font-weight:600;color:var(--brand);display:flex;align-items:center;gap:6px}
.callout .num{color:#333}
.social-dots{left:772px;top:32px;display:flex;gap:6px}
.social-dots span{width:17px;height:17px;border-radius:50%;background:#7b7f85}
.social-dots span.on{background:var(--brand)}
.login{left:890px;top:25px;width:153px;height:33px;border:1px solid var(--brand-mid);font-size:10px;letter-spacing:.6px;color:var(--brand);display:flex;align-items:center;justify-content:center;gap:5px;background:var(--white)}
.main-nav{left:380px;top:78px;display:flex;gap:25px;font-size:11.5px;color:#444}
.main-nav a{color:inherit;text-decoration:none;position:relative;padding-bottom:20px}
.main-nav a.current{color:var(--brand)}
.main-nav a.current::after{content:"";position:absolute;left:-6px;right:-6px;bottom:0;height:2px;background:var(--brand)}

/* hero */
.hero-side{top:119px;height:361px;background:linear-gradient(135deg,#c9ccd0,#e7e8ea 60%,#b7bbc1)}
.hero-side.left{left:0;width:156px}
.hero-side.right{left:1044px;width:156px}
.hero-photo{left:156px;top:119px;width:888px;height:361px;background:linear-gradient(135deg,#6b6a5c 0%,#3a3b38 45%,#7a7560 80%,#4b4a42 100%)}
.hero-title{left:156px;top:232px;width:888px;font-size:38px;font-weight:700;color:var(--white);letter-spacing:.5px}
.hero-copy{left:310px;top:282px;width:580px;font-size:13px;line-height:17px;color:var(--white)}
.hero-btn{left:535px;top:340px;width:128px;height:32px;background:var(--white);color:var(--brand);font-size:10px;font-weight:700;letter-spacing:1px;display:flex;align-items:center;justify-content:center}
.hero-dots{left:570px;top:437px;display:flex;gap:6px}
.hero-dots span{width:9px;height:9px;border-radius:50%;border:1.5px solid var(--white)}
.hero-dots span.on{background:var(--brand-mid);border-color:var(--brand-mid)}
.slide-tab{top:247px;width:32px;height:104px;border:1px solid var(--brand-mid);font-size:10px;font-weight:700;display:flex;flex-direction:column;align-items:center;justify-content:center;gap:6px;line-height:1}
.slide-tab.prev{left:50px;background:rgba(255,255,255,.25);color:var(--brand)}
.slide-tab.next{left:1117px;background:var(--brand-mid);color:var(--white)}

/* services */
.intro-title{left:0;top:536px;width:1200px;font-size:27px;font-weight:300;line-height:38px;color:#222}
.intro-sub{left:0;top:619px;width:1200px;font-size:13.5px;color:var(--muted)}
.double-rule{left:156px;top:665px;width:888px;height:5px;border-top:1px solid #d8dbe0;border-bottom:1px solid #d8dbe0}
.service{top:703px;width:200px;text-align:center}
.service .icon{width:80px;height:80px;margin:0 auto;border-radius:50%;border:1.5px solid var(--brand-mid);display:flex;align-items:center;justify-content:center;background:var(--white)}
.service .icon.active{background:var(--brand-mid)}
.service h3{margin-top:23px;font-size:13.5px;font-weight:600;color:#222;letter-spacing:.3px}
.service p{margin:8px auto 0;width:190px;font-size:11.5px;line-height:17.5px;color:#555}
.service .more{margin:20px auto 0;width:96px;height:24px;border:1px solid var(--brand-mid);font-size:9.5px;font-weight:700;letter-spacing:1px;color:var(--brand);display:flex;align-items:center;justify-content:center}
.service .more.active{background:var(--brand-mid);color:var(--white)}

/* feature split */
.feature-photo{left:0;top:990px;width:600px;height:440px;background:linear-gradient(140deg,#8a8670 0%,#3d3e3b 40%,#5c5a4b 75%,#9a9276 100%)}
.feature-panel{left:600px;top:990px;width:600px;height:440px;background:linear-gradient(135deg,#f0f1f3,#e1e3e6 55%,#eceef0)}
.feature-title{left:665px;top:1048px;width:400px;font-size:23px;line-height:30px;color:#222}
.feature-rule{left:665px;top:1133px;width:302px;height:1px;background:#c8cbd0}
.feature-copy{left:665px;top:1174px;width:400px;font-size:11.5px;line-height:17.5px;color:#555}
.feature-copy p+p{margin-top:17px}
.feature-btn{left:663px;top:1330px;width:143px;height:33px;background:var(--brand-mid);color:var(--white);font-size:10px;font-weight:700;letter-spacing:1px;display:flex;align-items:center;justify-content:center}

/* message */
.msg-rule{top:1496px;height:5px;border-top:1px solid #d8dbe0;border-bottom:1px solid #d8dbe0}
.msg-title{left:0;top:1488px;width:1200px;font-size:14px;font-weight:600;letter-spacing:1px;color:#222}
.field{height:30px;background:var(--field);font-size:11px;color:#9aa0a6;padding:9px 14px}
.field.area{height:118px}
.send{left:537px;top:1728px;width:96px;height:25px;background:var(--brand-mid);color:var(--white);font-size:9.5px;font-weight:700;letter-spacing:1px;display:flex;align-items:center;justify-content:center}

/* contact band */
.contact-band{left:20px;top:1818px;width:1158px;height:323px;background:var(--band-bg)}
.contact-title{left:0;top:1843px;width:1200px;font-size:23px;color:#222}
.contact-sub{left:0;top:1877px;width:1200px;font-size:13.5px;color:var(--muted)}
.info{top:1933px;width:280px;text-align:center}
.info .ring{width:82px;height:82px;margin:0 auto;border-radius:50%;border:1.5px solid var(--brand-mid);display:flex;align-items:center;justify-content:center}
.info h4{margin-top:21px;font-size:13.5px;font-weight:400;color:#222}
.info p{margin-top:9px;font-size:12px;line-height:18px;color:#555}
.info .phone{margin-top:6px;font-size:18.5px;color:#333}
.info .mail{font-size:12px;color:#555;text-decoration:underline}
.follow{margin-top:9px;display:flex;justify-content:center;align-items:center;gap:8px;color:#555;font-size:14px}
.follow i{width:12px;height:12px;background:#444;display:block}
.follow i.blue{background:var(--brand-mid)}

/* footer */
.site-footer{left:0;top:2141px;width:1200px;height:41px;background:var(--footer);color:var(--white);font-size:11px;padding:12px 0 0 155px}
.to-top{left:1004px;top:2124px;width:43px;height:58px;background:var(--brand-mid);display:flex;align-items:center;justify-content:center}
</style>
</head>
<body>

<header class="abs site-header">
  <div class="abs brand-name"><span class="brand-mark"></span><span>Harborline finish works</span></div>
  <div class="abs callout">Call Us
    <svg width="16" height="16" viewBox="0 0 24 24"><circle cx="12" cy="12" r="10.5" fill="none" stroke="#0255a3" stroke-width="2"/><path d="M8 7l2 0 1 3-1.5 1a7 7 0 003 3l1-1.5 3 1v2a1 1 0 01-1 1A9 9 0 017 8a1 1 0 011-1z" fill="#0255a3"/></svg>
    <span class="num">555.014.2290</span></div>
  <div class="abs social-dots"><span></span><span class="on"></span><span></span><span></span></div>
  <div class="abs login">
    <svg width="9" height="10" viewBox="0 0 10 11"><circle cx="5" cy="3" r="2.5" fill="#0255a3"/><path d="M0 11a5 5 0 0110 0z" fill="#0255a3"/></svg>
    LOGIN / REGISTER</div>
  <nav class="abs main-nav">
    <a class="current">HOME</a><a>ABOUT US</a><a>LASER ENGRAVING</a><a>LASER CUTTING</a><a>PART MARKING</a><a>COATINGS</a><a>CONTACT US</a>
  </nav>
</header>

<section>
  <div class="abs hero-side left" role="img" aria-label="Faded preview of previous slide photograph"></div>
  <div class="abs hero-side right" role="img" aria-label="Faded preview of next slide photograph"></div>
  <div class="abs hero-photo" role="img" aria-label="Photograph of laser engraved firearm parts on tactical gear"></div>
  <h1 class="abs hero-title center">LASER ENGRAVING</h1>
  <p class="abs hero-copy center">Capabilities Statement: With our selection of CO2 and fiber lasers there are very few materials and substrates that we cannot mark or engrave...</p>
  <div class="abs hero-btn">READ MORE</div>
  <div class="abs hero-dots"><span></span><span></span><span class="on"></span><span></span><span></span></div>
  <div class="abs slide-tab prev"><span>P</span><span>R</span><span>E</span><span>V</span></div>
  <div class="abs slide-tab next"><span>N</span><span>E</span><span>X</span><span>T</span></div>
</section>

<section>
  <h2 class="abs intro-title center">There are Many Variations of Passages<br>Lorem Ipsum Available</h2>
  <p class="abs intro-sub center">Contrary to popular belief, Lorem Ipsum is not simply random text It has roots in a piece</p>
  <div class="abs double-rule"></div>

  <div class="abs service" style="left:159px">
    <div class="icon"><svg width="30" height="30" viewBox="0 0 30 30" fill="none" stroke="#3176b5" stroke-width="1.6"><rect x="5" y="7" width="18" height="18"/><path d="M12 18l1-4 11-11 3 3-11 11z"/></svg></div>
    <h3>LASER ENGRAVING</h3>
    <p>Capabilities Statement: With our selection of CO2 and fiber lasers there are ...</p>
    <div class="more">READ MORE</div>
  </div>
  <div class="abs service" style="left:387px">
    <div class="icon active"><svg width="32" height="32" viewBox="0 0 32 32" fill="none" stroke="#fff" stroke-width="1.6"><circle cx="10" cy="24" r="4"/><circle cx="22" cy="24" r="4"/><path d="M12 21L22 4M20 21L10 4"/></svg></div>
    <h3>LASER CUTTING</h3>
    <p>Laser cutting is a non contact cutting process with a kurff width of 0.010...</p>
    <div class="more active">READ MORE</div>
  </div>
  <div class="abs service" style="left:614px">
    <div class="icon"><svg width="32" height="32" viewBox="0 0 32 32" fill="none" stroke="#3176b5" stroke-width="1.6"><path d="M6 22L22 6l4 4L10 26H6z"/><path d="M6 6l4-2 18 18-2 4z"/></svg></div>
    <h3>PART MARKING</h3>
    <p>Barcodes, 2d Data Matrix UID Marking, Name plates Id tags Asset locator tags...</p>
    <div class="more">READ MORE</div>
  </div>
  <div class="abs service" style="left:843px">
    <div class="icon"><svg width="34" height="34" viewBox="0 0 34 34" fill="none" stroke="#3176b5" stroke-width="1.6"><path d="M17 6L30 12 17 18 4 12z"/><path d="M4 17l13 6 13-6M4 22l13 6 13-6"/></svg></div>
    <h3>COATINGS</h3>
    <p>Duraglaze is a spray on ceramic based finish that can be applied to metals ...</p>
    <div class="more">READ MORE</div>
  </div>
</section>

<section>
  <div class="abs feature-photo" role="img" aria-label="Photograph of a rifle with ammunition on tactical vest"></div>
  <div class="abs feature-panel" role="img" aria-label="Soft grey background photograph of equipment"></div>
  <h2 class="abs feature-title">Contrary to popular belief, Lorem<br>Ipsum is not simply</h2>
  <div class="abs feature-rule"></div>
  <div class="abs feature-copy">
    <p>There are many variations of passages of Lorem Ipsum available, but the majority have suffered alteration in some form, by injected humour, or randomised words which don't look even slightly believable. If you are going to use a passage.</p>
    <p>of Lorem Ipsum, you need to be sure there isn't anything embarrassing hidden in the middle of text...</p>
  </div>
  <div class="abs feature-btn">DISCOVER MORE</div>
</section>

<section>
  <div class="abs msg-rule" style="left:156px;width:370px"></div>
  <div class="abs msg-rule" style="left:674px;width:370px"></div>
  <h2 class="abs msg-title center">SEND US MESSAGE</h2>
  <div class="abs field" style="left:233px;top:1537px;width:243px">Type you Name</div>
  <div class="abs field" style="left:496px;top:1537px;width:243px">Enter your Email</div>
  <div class="abs field" style="left:759px;top:1537px;width:208px">Phone</div>
  <div class="abs field area" style="left:233px;top:1587px;width:734px">Type your Message</div>
  <div class="abs send">SEND</div>
</section>

<section>
  <div class="abs contact-band"></div>
  <h2 class="abs contact-title center">Have&nbsp; Question? Contact Us</h2>
  <p class="abs contact-sub center">But I must explain to you how all this mistaken idea of denouncing</p>
  <div class="abs info" style="left:158px">
    <div class="ring"><svg width="22" height="26" viewBox="0 0 22 26"><path d="M11 1a9 9 0 019 9c0 7-9 15-9 15S2 17 2 10a9 9 0 019-9z" fill="#0255a3"/><circle cx="11" cy="10" r="3.4" fill="#fff"/></svg></div>
    <h4>Come Visit Us!</h4>
    <p>418 Keel Street #7, Portview,<br>WA 98000</p>
  </div>
  <div class="abs info" style="left:461px">
    <div class="ring"><svg width="22" height="22" viewBox="0 0 24 24"><path d="M5 3h4l2 5-2.5 1.5a11 11 0 006 6L16 13l5 2v4a2 2 0 01-2 2A17 17 0 013 5a2 2 0 012-2z" fill="#0255a3"/></svg></div>
    <h4>Contact Us Today!</h4>
    <div class="phone">Call Us: 555.014.2290</div>
    <div class="mail">hello@harborlinefinish.example</div>
  </div>
  <div class="abs info" style="left:763px">
    <div class="ring"><svg width="24" height="24" viewBox="0 0 24 24" fill="#0255a3"><circle cx="18" cy="5" r="3.5"/><circle cx="6" cy="12" r="3.5"/><circle cx="18" cy="19" r="3.5"/><path d="M6 12L18 5M6 12l12 7" stroke="#0255a3" stroke-width="2"/></svg></div>
    <h4>Foolow Us!</h4>
    <div class="follow"><i></i>/<i class="blue"></i>/<i></i>/<i></i></div>
  </div>
</section>

<footer class="abs site-footer">© 2018 Harborline finish works. All Right Reserved.&nbsp; | &nbsp;Privacy Policy&nbsp; | &nbsp;Terms &amp; Conditions</footer>
<div class="abs to-top"><svg width="14" height="16" viewBox="0 0 14 16" fill="none" stroke="#fff" stroke-width="1.8"><path d="M7 15V2M2 7l5-5 5 5"/></svg></div>

</body>
</html>
```